Search and Rescue Volunteer Profiles

We have 38 search and rescue volunteers and we need to create individual profile pages for an upcoming event. We want these to represent our brand and look similar to other work we have created but with new content. I have included a poster that we have used in the past to highlight volunteers (used for an ad campaign--which we aren't doing this time) but we want it changed up a bit. WE want their name, SR#, the year they joined the team and a few funny facts about them. This poster should show strength while also representing humanity (and a little humor). I'm picturing grid like background and strong colors. Also including our 25th anniversary logo which should be included.

```html
<!DOCTYPE html>
<html lang="en">
<head>
<meta charset="UTF-8">
<title>Volunteer Profile – Dan Harlow</title>
<link href="https://fonts.googleapis.com/css2?family=Oswald:wght@400;500&family=Montserrat:wght@700;800&family=Lato:wght@400&family=Black+Ops+One&display=swap" rel="stylesheet">
<style>
  :root {
    --backdrop: #5b5b5b;
    --paper: #ffffff;
    --ink: #111111;
    --crimson: #c8103e;
    --crimson-deep: #8a0a2a;
    --night: #1a0509;
    --photo-light: #e6e6e6;
    --photo-mid: #6e6e6e;
    --photo-dark: #0d0d0d;
  }
  * { margin: 0; padding: 0; box-sizing: border-box; }
  html, body {
    width: 1200px; height: 1200px; overflow: hidden;
    background: var(--backdrop);
  }
  .poster {
    position: absolute; left: 190px; top: 41px;
    width: 820px; height: 1118px;
    overflow: hidden;
    background: var(--paper);
  }
  .portrait {
    position: absolute; left: 0; top: 0; width: 620px; height: 100%;
    background:
      radial-gradient(ellipse 60% 45% at 40% 45%, rgba(60,60,60,0.55) 0%, rgba(60,60,60,0) 100%),
      linear-gradient(180deg, var(--photo-light) 0%, #d2d2d2 18%, #9a9a9a 40%, var(--photo-mid) 58%, #2b2b2b 80%, var(--photo-dark) 100%);
  }
  .brand-panel {
    position: absolute; left: 440px; top: 0; width: 380px; height: 340px;
    background: linear-gradient(90deg, rgba(255,255,255,0) 0%, var(--paper) 45%);
  }
  .brand-mark {
    position: absolute; left: 530px; top: 82px; width: 240px;
    text-align: center;
    font-family: 'Montserrat', sans-serif; font-weight: 800;
    color: var(--crimson);
  }
  .brand-mark .dot {
    width: 96px; height: 96px; border-radius: 50%;
    background: var(--crimson); margin: 0 auto 14px;
  }
  .brand-mark .brand-name {
    font-size: 17px; line-height: 1.25; letter-spacing: 1px; text-transform: uppercase;
  }
  .profile-panel {
    position: absolute; left: 466px; top: 331px; width: 354px; bottom: 0;
    background: linear-gradient(180deg, var(--paper) 0%, #f3d3dc 8%, var(--crimson) 22%, var(--crimson) 52%, var(--crimson-deep) 78%, var(--night) 100%);
  }
  .volunteer-name {
    position: absolute; left: 466px; width: 354px; top: 366px;
    text-align: center;
    font-family: 'Oswald', sans-serif; font-weight: 500;
    font-size: 62px; line-height: 1; color: var(--ink);
    letter-spacing: -1px;
  }
  .volunteer-id {
    position: absolute; left: 466px; width: 354px; top: 462px;
    text-align: center; color: var(--paper);
    font-family: 'Montserrat', sans-serif; font-weight: 800;
    font-size: 34px; line-height: 1;
  }
  .volunteer-since {
    position: absolute; left: 466px; width: 354px; top: 502px;
    text-align: center; color: var(--paper);
    font-family: 'Montserrat', sans-serif; font-weight: 700;
    font-size: 21px; line-height: 1;
  }
  .volunteer-bio {
    position: absolute; left: 506px; width: 268px; top: 564px;
    color: var(--paper);
    font-family: 'Lato', sans-serif; font-size: 17.5px; line-height: 23.6px;
    letter-spacing: -0.3px; word-spacing: -0.5px;
    text-align: justify; hyphens: manual;
  }
  .headline-top {
    position: absolute; left: 333px; top: 825px;
    font-family: 'Oswald', sans-serif; font-weight: 400;
    font-size: 96px; line-height: 1; color: var(--paper);
    letter-spacing: -2px;
  }
  .headline-main {
    position: absolute; left: 211px; top: 912px;
    font-family: 'Black Ops One', sans-serif;
    font-size: 165px; line-height: 1; color: var(--paper);
    letter-spacing: 2px;
  }
  .site-url {
    position: absolute; left: 418px; top: 1060px;
    font-family: 'Lato', sans-serif; font-size: 20px;
    letter-spacing: 4.6px; color: var(--paper);
  }
</style>
</head>
<body>
  <main class="poster">
    <div class="portrait" role="img" aria-label="Black and white portrait photo of the volunteer in a cap and work shirt"></div>
    <div class="brand-panel"></div>
    <div class="brand-mark">
      <div class="dot"></div>
      <p class="brand-name">Alder Peak<br>Search and Rescue</p>
    </div>
    <div class="profile-panel"></div>
    <h1 class="volunteer-name">DAN HARLOW</h1>
    <p class="volunteer-id">SR#47</p>
    <p class="volunteer-since">VOLUNTEER SINCE 2000</p>
    <p class="volunteer-bio">Lorem Ipsum is simply dummy text of the printing and type&shy;setting industry. Lorem Ipsum has been the industry's stand&shy;ard dummy text ever since the 1500s, when an unknown printer took a galley of type and scrambled it to make a type specimen book.</p>
    <p class="headline-top">UPCOMING</p>
    <p class="headline-main">EVENT</p>
    <p class="site-url">www.alderpeaksar.org</p>
  </main>
</body>
</html>
```